OLVAK Web Design (Need help to re-design our website)

We need someone to help us re-design our website and launch it. All contents for the website are ready. (https://olvak.example.au/)

-Rearrange categories:
1. Heating & Cooling
2. Remove Home Appliance
3. Remove Entertainment

Home page - redesign (It will be a nice touch if the banner is in the loop).

NOTE:
-Brand colour blue and orange.
-Try using professional fonts (Example: Helvetica, etc.)
-The website's Footer should be readable and use light colour.

Target Market(s)

Residentials & commercial buildings

Industry/Entity Type

Heat Ventilation and Cooling Industry, Technology , Renewables

Coding

Coded - Design and coding required

Colors
0094D4
00A9DD
6FCCEA
C7EBF8
E9F6FB
59FF00
82FF00
B8FF75
E3FFCB
F4FFEA
F0912C
F2A743
F7CA91
FBE8D2
FDF5EE

Requirements
Nice to have
• Effects/transition on the words/copy/images.

```html
<!DOCTYPE html>
<html lang="en">
<head>
<meta charset="utf-8">
<title>OLVAK – Heating &amp; Cooling</title>
<link rel="stylesheet" href="https://fonts.googleapis.com/css2?family=Roboto:wght@400;500;700;900&family=Open+Sans:wght@300;400;600;700&family=Montserrat:wght@800;900&family=Bebas+Neue&family=Noto+Serif:wght@400&display=swap">
<style>
:root{
  --blue:#0f62b8;
  --blue-bright:#1a73c9;
  --orange:#f0912c;
  --orange-deep:#f7941d;
  --ink:#1d1d1d;
  --body:#3c3c3c;
  --muted:#5d5d5d;
  --pale:#eef4fb;
  --card:#f3f6fa;
  --dark:#141414;
  --band:#474747;
  --footer:#111111;
  --teal:#1eb6a4;
}
*{box-sizing:border-box;margin:0;padding:0}
html,body{width:1200px;height:2981px;overflow:hidden}
body{position:relative;background:#fff;font-family:"Open Sans",Helvetica,Arial,sans-serif;color:var(--body)}
.abs{position:absolute}
.btn{display:inline-block;background:var(--blue);color:#fff;font-family:"Roboto",Arial,sans-serif;font-weight:500;border-radius:3px;text-align:center}

/* top bar */
.topbar{left:0;top:0;width:1200px;height:36px;background:#0e0e0e;color:#fff;font-family:Arial,Helvetica,sans-serif;font-size:11px}
.topbar .contact{left:62px;top:11px;display:flex;align-items:center;gap:8px}
.topbar .sep{width:1px;height:18px;background:#888;margin:0 6px}
.topbar .social{right:62px;top:9px;display:flex;gap:4px}
.topbar .social span{width:18px;height:18px;background:#fff;border-radius:2px;display:block}

/* nav */
.nav{left:0;top:36px;width:1200px;height:54px;background:#fffaf4;border-bottom:1px solid #e6e6e6}
.brand{font-family:"Roboto",Arial,sans-serif;font-weight:900;letter-spacing:5px;color:var(--blue);display:flex;align-items:center;gap:10px}
.brand i{display:block;background:var(--orange)}
.nav .brand{left:62px;top:10px;font-size:30px}
.nav .brand i{width:26px;height:26px}
.nav .menu{left:419px;top:18px;display:flex;gap:28px;font-family:"Roboto",Arial,sans-serif;font-size:14px;color:#222}
.nav .menu b{font-weight:700}
.nav .search{left:982px;top:12px;width:26px;height:29px;background:var(--orange);border-radius:3px}
.nav .book{left:1014px;top:12px;width:124px;height:29px;line-height:29px;font-size:12.5px}

/* hero */
.hero{left:0;top:90px;width:1200px;height:458px;background:linear-gradient(100deg,#0b2d3a 0%,#0f4a5a 35%,#1a5766 60%,#2c4a5a 80%,#1c2f3c 100%)}
.hero .arrow{top:214px;width:32px;height:32px;background:rgba(255,255,255,.08);border:1px solid rgba(255,255,255,.15)}
.hero .arrow svg{display:block;margin:8px auto}
.hero .eyebrow{left:0;width:1200px;top:220px;text-align:center;color:#fff;font-family:Arial,Helvetica,sans-serif;font-size:23px;letter-spacing:1px}
.hero .headline{left:0;width:1200px;top:247px;text-align:center;color:var(--orange-deep);font-family:"Montserrat",Arial,sans-serif;font-weight:900;font-size:49px;letter-spacing:1px}
.hero .subline{left:0;width:1200px;top:300px;text-align:center;color:#fff;font-family:"Open Sans",sans-serif;font-weight:600;font-size:37px}
.hero .explore{left:551px;top:356px;width:86px;height:35px;line-height:35px;font-size:14px;font-weight:700}
.hero .dots{left:540px;top:434px;display:flex;gap:6px}
.hero .dots span{width:25px;height:2px;background:rgba(255,255,255,.4)}
.hero .dots span.on{width:48px;background:var(--orange)}

/* compliance */
.compliance{left:0;top:548px;width:1200px;height:134px;background:var(--pale)}
.compliance .l1{left:215px;top:28px;font-size:36px;font-weight:300;color:#111}
.compliance .l2{left:215px;top:70px;font-family:"Roboto",Arial,sans-serif;font-size:29px;font-weight:700;color:#111}
.badge{top:20px;width:94px;height:94px;border-radius:50%}

/* story */
.story-photo{left:62px;top:736px;width:574px;height:429px;border-radius:6px;background:linear-gradient(120deg,#e7b17c 0%,#f07a22 35%,#c9c0b4 60%,#7b7470 100%)}
.guarantee-shadow{left:344px;top:1095px;width:288px;height:112px;background:#111;border-radius:6px}
.guarantee{left:350px;top:1089px;width:286px;height:112px;background:var(--blue);border-radius:6px;color:#fff;font-family:"Roboto",Arial,sans-serif;font-size:29px;line-height:38px;padding:18px 22px}
.guarantee b{font-weight:700}
.story h2{position:absolute;left:660px;top:778px;font-family:"Noto Serif",Georgia,serif;font-weight:400;font-size:34px;color:#111}
.story p{position:absolute;left:661px;width:460px;font-size:12.8px;line-height:20.6px;color:#333}
.story .readmore{left:660px;top:1078px;width:93px;height:35px;line-height:35px;font-size:12.5px;font-weight:700}

/* speciality */
.special{left:0;top:1246px;width:1200px;height:386px;background:radial-gradient(ellipse at 25% 40%,#2b2b2b 0%,#141414 60%,#0c0c0c 100%)}
.special .kicker{left:0;width:1200px;top:58px;text-align:center;color:var(--orange-deep);font-family:"Roboto",Arial,sans-serif;font-weight:700;font-size:15px}
.special h2{position:absolute;left:0;width:1200px;top:90px;text-align:center;color:#fff;font-family:"Bebas Neue",Impact,sans-serif;font-weight:400;font-size:32px;line-height:38px;letter-spacing:.5px}
.help{left:62px;top:1458px;width:262px;height:312px;background:linear-gradient(180deg,#3a3836 0%,#222 60%,#2d2a28 100%)}
.help .small{left:17px;top:137px;color:#fff;font-family:"Bebas Neue",Impact,sans-serif;font-size:13px;letter-spacing:.4px}
.help .big{left:17px;top:152px;color:#fff;font-family:"Roboto",Arial,sans-serif;font-weight:700;font-size:20px}
.help .tags{left:59px;top:266px;width:145px;height:30px;display:flex;border-radius:2px;overflow:hidden;font-family:"Bebas Neue",Impact,sans-serif;font-size:13px}
.help .tags span{flex:1;display:flex;align-items:center;justify-content:center}
.help .tags .t1{background:var(--blue);color:#fff}
.help .tags .t2{background:#fff;color:var(--orange)}
.svc{top:1458px;width:265px;height:312px;background:#fff;border:1px solid #e4e4e4}
.svc .pic{height:172px}
.svc h3{position:absolute;left:10px;top:184px;font-family:"Roboto",Arial,sans-serif;font-weight:500;font-size:14.5px;color:#222}
.svc p{position:absolute;left:10px;top:212px;width:245px;font-size:8.7px;line-height:13px;color:#555}
.svc a{position:absolute;left:10px;top:287px;font-size:8.5px;color:var(--blue);text-decoration:none}

/* why choose */
.why .label{left:160px;top:1882px;font-size:10px;color:#444}
.why h2{position:absolute;left:160px;top:1898px;width:270px;font-family:"Open Sans",sans-serif;font-weight:700;font-size:25px;line-height:30px;color:#444}
.why .intro{left:160px;top:1967px;width:250px;font-size:10.5px;line-height:17px;color:#555}
.feature{background:var(--card);padding:12px 14px}
.feature h3{display:flex;align-items:center;gap:8px;font-family:"Roboto",Arial,sans-serif;font-weight:700;font-size:14.5px;color:var(--blue)}
.feature h3 i{display:block;width:20px;height:20px;border-radius:50%;background:var(--orange)}
.feature p{font-size:10.5px;line-height:15px;color:#444;margin-top:10px}
.dotgrid{fill:var(--teal)}

/* testimonials */
.tst-photo{left:62px;top:2120px;width:368px;height:349px;background:linear-gradient(135deg,#e6cfa3 0%,#d7b98a 45%,#3f5f8f 70%,#2c4670 100%)}
.tst .quote{left:462px;top:2137px}
.tst .label{left:463px;top:2174px;font-size:10.5px;color:#444}
.tst h2{position:absolute;left:463px;top:2190px;font-weight:600;font-size:25px;color:#333}
.tst .intro{left:463px;top:2228px;font-size:11.4px;color:#555}
.review{top:2260px;width:320px;height:161px;background:var(--card);padding:18px 12px}
.review p{font-size:13.8px;line-height:20.5px;color:#777;font-weight:300}
.review .who{position:absolute;left:12px;top:91px;display:flex;align-items:center;gap:12px}
.review .avatar{width:56px;height:56px;border-radius:50%;background:linear-gradient(135deg,#c97a3a,#6a4a36)}
.review .name{font-family:"Roboto",Arial,sans-serif;font-weight:500;font-size:14px;color:#333}
.review .role{font-family:"Roboto",Arial,sans-serif;font-size:12px;color:#555;margin-top:3px}

/* question band */
.ask{left:0;top:2543px;width:1200px;height:170px;background:var(--band)}
.ask .q{left:85px;top:46px;color:#fff;font-family:"Roboto",Arial,sans-serif;font-weight:700;font-size:39px}
.ask .call{left:85px;top:94px;color:#fff;font-family:"Roboto",Arial,sans-serif;font-size:28px}
.ask .cb{left:979px;top:69px;width:138px;height:36px;line-height:36px;border-radius:18px;font-size:13px;background:var(--blue-bright)}

/* footer */
.footer{left:0;top:2713px;width:1200px;height:235px;background:var(--footer);color:#fff}
.footer .brand{left:80px;top:42px;color:#fff;font-size:33px}
.footer .brand i{width:30px;height:30px;background:#fff}
.footer .about{left:80px;top:104px;width:322px;font-size:10px;line-height:16.3px;text-align:justify}
.footer h4{position:absolute;top:56px;font-family:"Roboto",Arial,sans-serif;font-weight:700;font-size:19px}
.footer ul{position:absolute;list-style:none;font-size:11px;line-height:20px}
.footer .circles{left:975px;top:98px;display:flex;gap:6px}
.footer .circles span{width:33px;height:33px;border-radius:50%;background:#fff;display:block}
.copy{left:0;top:2948px;width:1200px;height:33px;background:#262626;color:#fff;font-size:10px;text-align:center;line-height:33px}
</style>
</head>
<body>

<div class="abs topbar">
  <div class="abs contact">
    <svg width="12" height="12" viewBox="0 0 24 24"><path d="M6.6 10.8a15 15 0 0 0 6.6 6.6l2.2-2.2c.3-.3.7-.4 1-.2 1.1.4 2.3.6 3.6.6.6 0 1 .4 1 1V20c0 .6-.4 1-1 1A17 17 0 0 1 3 4c0-.6.4-1 1-1h3.5c.6 0 1 .4 1 1 0 1.3.2 2.5.6 3.6.1.3 0 .7-.2 1z" fill="#f0912c"/></svg>
    <span><b>Call</b> 1800 555 019</span>
    <span class="sep"></span>
    <svg width="12" height="12" viewBox="0 0 24 24"><circle cx="12" cy="12" r="9" fill="none" stroke="#f0912c" stroke-width="2.4"/><circle cx="12" cy="12" r="3.5" fill="none" stroke="#f0912c" stroke-width="2.4"/></svg>
    <span>info@olvak.example.au</span>
  </div>
  <div class="abs social"><span></span><span></span><span></span></div>
</div>

<header class="abs nav">
  <div class="abs brand"><i></i>OLVAK</div>
  <nav class="abs menu"><b>Home</b><span>Heating &amp; Cooling</span><span>Our Story</span><span>Support</span></nav>
  <div class="abs search"><svg width="26" height="29" viewBox="0 0 26 29"><circle cx="12" cy="13" r="5" fill="none" stroke="#222" stroke-width="1.8"/><path d="M15.5 16.5l4 4" stroke="#222" stroke-width="1.8"/></svg></div>
  <div class="abs btn book">Book Appointment</div>
</header>

<section class="abs hero" role="img" aria-label="Technician servicing an air conditioning unit with digital overlay graphics">
  <div class="abs arrow" style="left:62px"><svg width="14" height="14" viewBox="0 0 14 14"><path d="M9 2L4 7l5 5" fill="none" stroke="#fff" stroke-width="1.4"/></svg></div>
  <div class="abs arrow" style="left:1105px"><svg width="14" height="14" viewBox="0 0 14 14"><path d="M5 2l5 5-5 5" fill="none" stroke="#fff" stroke-width="1.4"/></svg></div>
  <div class="abs eyebrow">REVOLUTIONISE</div>
  <div class="abs headline">HEATING &amp; COOLING</div>
  <div class="abs subline">Industry Australiawide</div>
  <div class="abs btn explore">Explore</div>
  <div class="abs dots"><span></span><span class="on"></span><span></span></div>
</section>

<section class="abs compliance">
  <div class="abs l1">Fully Compliant with all</div>
  <div class="abs l2">Government Rebates</div>
  <div class="abs badge" style="left:626px;background:#c9a02c"></div>
  <div class="abs badge" style="left:759px;background:#1e3f8a"></div>
  <div class="abs badge" style="left:888px;background:#e7e7e7"></div>
</section>

<section class="story">
  <div class="abs story-photo" role="img" aria-label="Two smiling technicians in hard hats and high-visibility vests beside an outdoor unit"></div>
  <div class="abs guarantee-shadow"></div>
  <div class="abs guarantee"><b>100%</b> Satisfaction<br>Guarantee</div>
  <h2>Our Story</h2>
  <p style="top:835px">OLVAK is a company dedicated to manufacturing and installing energy-efficient products that reduce energy consumption, save costs, and promote sustainability. Our mission is to help individuals and businesses reduce their carbon footprint while also enhancing their comfort and quality of life.</p>
  <p style="top:937px">Our story began with a group of like-minded individuals who saw the urgent need to address climate change and the impact of energy consumption on the environment. We recognized that energy-efficient products were not only good for the planet but also for individuals’ wallets. We believed that we could make a difference by developing and providing accessible and affordable energy-efficient solutions.</p>
  <div class="abs btn readmore">Read More</div>
</section>

<section class="abs special" role="img" aria-label="Dark backdrop of refrigerant pressure gauges">
  <div class="abs kicker">SOME OF OUR SPECIALITY</div>
  <h2>The high standard trusted &amp;<br>professional service</h2>
</section>

<div class="abs help" role="img" aria-label="Technician working on heating equipment">
  <div class="abs small">OPEN 24/7 WITH OFFICE STAFF</div>
  <div class="abs big">How Can We Help You?</div>
  <div class="abs tags"><span class="t1">HEATING</span><span class="t2">COOLING</span></div>
</div>

<article class="abs svc" style="left:331px">
  <div class="pic" role="img" aria-label="Technician installing a heat pump" style="background:linear-gradient(135deg,#c9c9c6,#8a7a6a 50%,#e2e2de)"></div>
  <h3>Heat Pump</h3>
  <p>Lorem ipsum dolor sit amet, consectetur adipiscing elit, sed do eiusmod tempor incididunt ut labore et dolore magna aliqua. Quis ipsum suspendisse ultrices gravida. Risus commodo viverra maecenas accumsan lacus vel facilisis.</p>
  <a>Read More</a>
</article>
<article class="abs svc" style="left:602px">
  <div class="pic" role="img" aria-label="Swimming pool with heat pump and garden" style="background:linear-gradient(180deg,#6f7a5a 0%,#3b6b3a 45%,#2f8ed8 70%,#7fbf4a 100%)"></div>
  <h3>Swimming Pool Heat Pump</h3>
  <p>Lorem ipsum dolor sit amet, consectetur adipiscing elit, sed do eiusmod tempor incididunt ut labore et dolore magna aliqua. Quis ipsum suspendisse ultrices gravida. Risus commodo viverra maecenas accumsan lacus vel facilisis.</p>
  <a>Read More</a>
</article>
<article class="abs svc" style="left:873px">
  <div class="pic" role="img" aria-label="Thermostatic radiator valve close-up" style="background:linear-gradient(135deg,#f3f1ee 0%,#cfc9c1 50%,#a89060 100%)"></div>
  <h3>Monoblock Heat Pump</h3>
  <p>Lorem ipsum dolor sit amet, consectetur adipiscing elit, sed do eiusmod tempor incididunt ut labore et dolore magna aliqua. Quis ipsum suspendisse ultrices gravida. Risus commodo viverra maecenas accumsan lacus vel facilisis.</p>
  <a>Read More</a>
</article>

<section class="why">
  <div class="abs label">WHY CHOOSE US</div>
  <h2>Relaxation and your satisfaction.</h2>
  <p class="abs intro">Lorem ipsum dolor sit amet, consectetur adipiscing elit. Ut elit tellus, luctus nec ullamcorper mattis, pulvinar dapibus leo.</p>
  <svg class="abs" style="left:955px;top:1818px" width="92" height="90">
    <g class="dotgrid">
      <circle cx="8" cy="4" r="1.3"/><circle cx="21" cy="4" r="1.3"/><circle cx="34" cy="4" r="1.3"/><circle cx="47" cy="4" r="1.3"/><circle cx="60" cy="4" r="1.3"/><circle cx="73" cy="4" r="1.3"/><circle cx="86" cy="4" r="1.3"/>
      <circle cx="8" cy="17" r="1.3"/><circle cx="21" cy="17" r="1.3"/><circle cx="34" cy="17" r="1.3"/><circle cx="47" cy="17" r="1.3"/><circle cx="60" cy="17" r="1.3"/><circle cx="73" cy="17" r="1.3"/><circle cx="86" cy="17" r="1.3"/>
      <circle cx="60" cy="30" r="1.3"/><circle cx="73" cy="30" r="1.3"/><circle cx="86" cy="30" r="1.3"/>
      <circle cx="60" cy="43" r="1.3"/><circle cx="73" cy="43" r="1.3"/><circle cx="86" cy="43" r="1.3"/>
      <circle cx="60" cy="56" r="1.3"/><circle cx="73" cy="56" r="1.3"/><circle cx="86" cy="56" r="1.3"/>
      <circle cx="60" cy="69" r="1.3"/><circle cx="73" cy="69" r="1.3"/><circle cx="86" cy="69" r="1.3"/>
      <circle cx="60" cy="82" r="1.3"/><circle cx="73" cy="82" r="1.3"/><circle cx="86" cy="82" r="1.3"/>
    </g>
  </svg>
  <div class="abs feature" style="left:452px;top:1850px;width:271px;height:90px"><h3><i></i>Quality Products</h3><p>We only offer high-quality products that are built to last.</p></div>
  <div class="abs feature" style="left:734px;top:1848px;width:271px;height:94px"><h3><i style="background:#3b7bd0"></i>Expert Installation</h3><p>Our team of experienced professionals will ensure that your heat pump water heater is installed correctly and safely.</p></div>
  <div class="abs feature" style="left:452px;top:1952px;width:271px;height:93px"><h3><i style="background:#e2574c"></i>Customer Service</h3><p>We pride ourselves on our excellent customer service and are always here to help you with any questions or concerns.</p></div>
</section>

<section class="tst">
  <div class="abs tst-photo" role="img" aria-label="Technician in blue overalls holding a clipboard beside a house"></div>
  <svg class="abs" style="left:436px;top:2355px" width="10" height="125"><g class="dotgrid"><circle cx="4" cy="4" r="1.5"/><circle cx="4" cy="20" r="1.5"/><circle cx="4" cy="36" r="1.5"/><circle cx="4" cy="52" r="1.5"/><circle cx="4" cy="68" r="1.5"/><circle cx="4" cy="84" r="1.5"/><circle cx="4" cy="100" r="1.5"/><circle cx="4" cy="116" r="1.5"/></g></svg>
  <svg class="abs" style="left:318px;top:2472px" width="120" height="10"><g class="dotgrid"><circle cx="6" cy="4" r="1.5"/><circle cx="26" cy="4" r="1.5"/><circle cx="46" cy="4" r="1.5"/><circle cx="66" cy="4" r="1.5"/><circle cx="86" cy="4" r="1.5"/><circle cx="106" cy="4" r="1.5"/></g></svg>
  <svg class="abs quote" width="30" height="24" viewBox="0 0 30 24"><path d="M12 3C6 4 2 8 2 14c0 4 2 7 5 7s5-2 5-5-2-5-5-5c0-3 2-5 5-6zM28 3c-6 1-10 5-10 11 0 4 2 7 5 7s5-2 5-5-2-5-5-5c0-3 2-5 5-6z" fill="none" stroke="#f0912c" stroke-width="2.4"/></svg>
  <div class="abs label">TESTIMONIAL</div>
  <h2>What client say about us.</h2>
  <div class="abs intro">Lorem ipsum dolor sit amet, consectetur adipiscing elit. Ut elit tellus, luctus nec ullamcorper mattis, pulvinar dapibus leo.</div>
  <div class="abs review" style="left:463px">
    <p>Ac efficitur quis sed est sapien euismod gravida hendrerit finibus si. Himenaeos dictumst velit etiam hendrerit aptent.</p>
    <div class="who"><div class="avatar" role="img" aria-label="Client portrait"></div><div><div class="name">Marcus Hale</div><div class="role">Businessman</div></div></div>
  </div>
  <div class="abs review" style="left:795px">
    <p>Ac efficitur quis sed est sapien euismod gravida hendrerit finibus si. Himenaeos dictumst velit etiam hendrerit aptent.</p>
    <div class="who"><div class="avatar" role="img" aria-label="Client portrait"></div><div><div class="name">Priya Lennon</div><div class="role">Blogger</div></div></div>
  </div>
</section>

<section class="abs ask">
  <div class="abs q">Have a question?</div>
  <div class="abs call">Call 1800 555 019</div>
  <div class="abs btn cb">Requrest CallBack</div>
</section>

<footer class="abs footer">
  <div class="abs brand"><i></i>OLVAK</div>
  <p class="abs about">OLVAK is a company dedicated to manufacturing and installing energy-efficient products that reduce energy consumption, save costs, and promote sustainability. Our mission is to help individuals and businesses reduce their carbon footprint while also enhancing their comfort and quality of life.</p>
  <h4 style="left:469px">Our Products</h4>
  <ul style="left:474px;top:86px"><li>Heating &amp; Cooling</li><li>Heat Pump</li><li>Air Conditioners</li><li>Swimming Pool Heat Pump</li><li>Monoblock Heat Pump</li></ul>
  <h4 style="left:676px">Useful Links</h4>
  <ul style="left:677px;top:89px"><li>Our Story</li><li>Support</li><li>Latest Promotions</li><li>Book Appointment</li><li>Privacy Policy</li></ul>
  <ul style="left:802px;top:89px"><li>Terms &amp; Conditions</li><li>Sitemap</li></ul>
  <h4 style="left:976px">Follow us</h4>
  <div class="abs circles"><span></span><span></span><span></span></div>
</footer>
<div class="abs copy">© Copyright 2024 OLVAK - All rights reserved.</div>

</body>
</html>
```